Flyer Design Project

Need a DL Size flyer (2 sided) for letter box marketing for our website www.brightwardsecure.com.au

Project Deadline Extended
Reason: Thank you for submitting the designs. We like few of the designs and will request those designers to changes few things to make it more suitable for us. Because of holidays need to extend the deadlines. Thank you.

Industry/Entity Type

Marketing

```html
<!DOCTYPE html>
<html lang="en">
<head>
<meta charset="utf-8">
<title>BrightwardSecure – Inside Spread</title>
<link href="https://fonts.googleapis.com/css2?family=Arimo:wght@400;700&family=Open+Sans:wght@400;600;700&display=swap" rel="stylesheet">
<style>
  :root {
    --stage: #3a3a3c;
    --navy: #1c4a78;
    --heading-blue: #123f6e;
    --yellow: #f9c832;
    --yellow-band: #fdcb2e;
    --orange: #f7a21f;
    --orange-light: #fcd05a;
    --cream: #f3efe2;
    --blue-deep: #272a85;
    --blue-mid: #1f4fb8;
    --blue-light: #3a9de4;
    --card: #ffffff;
    --rule: #e6e6e6;
    --ink: #333333;
    --muted: #9a9a9a;
    --btn-top: #9cc446;
    --btn-bottom: #76a22a;
  }
  * { box-sizing: border-box; margin: 0; padding: 0; }
  html, body { width: 1200px; height: 1027px; overflow: hidden; }
  body { background: var(--stage); position: relative; font-family: "Arimo", Arial, sans-serif; }

  .spread { position: absolute; left: 58px; top: 90px; width: 1089px; height: 823px; }

  /* Panels */
  .panel { position: absolute; top: 0; height: 823px; overflow: hidden; }
  .panel-about { left: 0; width: 359px; background: radial-gradient(circle at 30% 70%, #fbf8ee 0%, var(--cream) 55%, #e9e3cf 100%); }
  .panel-packages { left: 359px; width: 364px; background: linear-gradient(180deg, var(--blue-deep) 0%, var(--blue-mid) 60%, var(--blue-light) 100%); }
  .panel-visit { left: 723px; width: 366px; background: linear-gradient(170deg, var(--orange-light) 0%, var(--orange) 45%, #f9b93a 75%, var(--orange) 100%); }

  /* About panel */
  .feature { position: absolute; left: 32px; width: 320px; }
  .feature-icon { position: absolute; left: 0; top: 0; width: 26px; height: 26px; }
  .feature-title { position: absolute; left: 36px; top: -2px; width: 250px; height: 22px; background: var(--yellow); color: var(--heading-blue); font-weight: 700; font-size: 17.5px; line-height: 22px; padding-left: 6px; }
  .feature-text { position: absolute; left: 42px; top: 23px; width: 252px; color: var(--navy); font-size: 17px; line-height: 21px; }
  .feature-about { top: 101px; }
  .feature-plans { top: 276px; }
  .feature-hardware { top: 432px; }
  .about-photo { position: absolute; left: 32px; top: 634px; width: 316px; height: 137px; border-radius: 4px; background: linear-gradient(90deg, #3b3f46 0%, #1d1f24 55%, #d9dde2 80%, #f1f2f4 100%); }

  /* Packages panel */
  .packages-title { position: absolute; left: 392px; top: 48px; z-index: 3; font-family: "Open Sans", sans-serif; font-weight: 600; font-size: 41px; color: transparent; -webkit-text-stroke: 1.4px var(--yellow); letter-spacing: -0.5px; }

  .package-sheet { position: absolute; left: 378px; top: 91px; width: 532px; height: 720px; background: var(--card); z-index: 2; }

  .package-row { position: absolute; display: grid; grid-template-columns: repeat(3, 1fr); border: 1px solid var(--rule); height: 322px; font-family: "Open Sans", sans-serif; }
  .package-row-dvr { left: 14px; top: 14px; width: 496px; }
  .package-row-ip { left: 19px; top: 376px; width: 489px; height: 316px; }
  .package { position: relative; border-right: 1px solid var(--rule); text-align: center; }
  .package:last-child { border-right: none; }
  .package-name { position: absolute; top: 8px; width: 100%; font-size: 12px; font-weight: 700; color: var(--ink); }
  .package-type { position: absolute; top: 34px; width: 100%; font-size: 7px; color: var(--muted); }
  .package-photo { position: absolute; left: 13px; right: 13px; top: 53px; height: 78px; border: 1px solid var(--rule); border-radius: 3px; background: linear-gradient(90deg, #d9dcdf 0%, #50555c 45%, #e9ebee 75%, #f6f6f7 100%); }
  .package-rule { position: absolute; left: 0; right: 0; height: 1px; background: var(--rule); }
  .rule-top { top: 134px; }
  .rule-bottom { top: 246px; }
  .package-specs { position: absolute; top: 143px; width: 100%; list-style: none; font-size: 6.6px; line-height: 11.3px; color: var(--ink); }
  .package-price { position: absolute; top: 258px; width: 100%; font-size: 13px; font-weight: 700; color: #444; }
  .package-gst { position: absolute; top: 277px; width: 100%; font-size: 8.5px; color: var(--muted); }
  .package-contact { position: absolute; left: 50%; top: 296px; width: 77px; height: 20px; margin-left: -38px; border-radius: 2px; background: linear-gradient(var(--btn-top), var(--btn-bottom)); color: #fff; font-size: 6.5px; line-height: 20px; }
  .package-row-ip .rule-bottom { top: 240px; }
  .package-row-ip .package-price { top: 252px; }
  .package-row-ip .package-gst { top: 271px; }
  .package-row-ip .package-contact { top: 290px; }

  /* Visit panel */
  .visit-band { position: absolute; left: 0; top: 0; width: 366px; height: 91px; background: var(--yellow-band); }
  .visit-icon { position: absolute; left: 695px; top: 26px; width: 54px; height: 54px; z-index: 4; }
  .visit-label { position: absolute; left: 43px; top: 36px; font-size: 17px; color: var(--heading-blue); }
  .visit-url { position: absolute; left: 43px; top: 57px; font-size: 19px; font-weight: 700; color: var(--heading-blue); letter-spacing: -0.3px; white-space: nowrap; }
  .visit-photo { position: absolute; left: 205px; top: 172px; width: 141px; height: 111px; border-radius: 3px; background: linear-gradient(180deg, #6b6f73 0%, #9b8c76 45%, #2a2b2e 80%, #1a1a1c 100%); }
  .visit-rule { position: absolute; left: 203px; top: 283px; width: 154px; height: 1px; background: var(--heading-blue); }
  .visit-text { position: absolute; left: 200px; top: 296px; width: 140px; font-size: 14px; line-height: 22px; font-weight: 700; color: var(--navy); }
</style>
</head>
<body>
<main class="spread">

  <section class="panel panel-about">
    <div class="feature feature-about">
      <svg class="feature-icon" viewBox="0 0 26 26"><circle cx="13" cy="13" r="11.5" fill="none" stroke="var(--heading-blue)" stroke-width="2.2"/><path d="M6.5 13h11M13 8l5 5-5 5" fill="none" stroke="var(--heading-blue)" stroke-width="2.4" stroke-linecap="round" stroke-linejoin="round"/></svg>
      <h2 class="feature-title">About Us</h2>
      <p class="feature-text">BrightwardSecure is dedicated to providing high quality CCTV System at affordable prices. All of our packages include hardware, software, accessories and full installation.</p>
    </div>
    <div class="feature feature-plans">
      <svg class="feature-icon" viewBox="0 0 26 26"><circle cx="13" cy="13" r="11.5" fill="none" stroke="var(--heading-blue)" stroke-width="2.2"/><path d="M6.5 13h11M13 8l5 5-5 5" fill="none" stroke="var(--heading-blue)" stroke-width="2.4" stroke-linecap="round" stroke-linejoin="round"/></svg>
      <h2 class="feature-title">Customized Plans</h2>
      <p class="feature-text">We offer a variety of CCTV system packages as well as we build custom system that suits your needs on the basis of size, location and budget.</p>
    </div>
    <div class="feature feature-hardware">
      <svg class="feature-icon" viewBox="0 0 26 26"><circle cx="13" cy="13" r="11.5" fill="none" stroke="var(--heading-blue)" stroke-width="2.2"/><path d="M6.5 13h11M13 8l5 5-5 5" fill="none" stroke="var(--heading-blue)" stroke-width="2.4" stroke-linecap="round" stroke-linejoin="round"/></svg>
      <h2 class="feature-title">Reliable Hardware</h2>
      <p class="feature-text">We only use high quality reliable hardware &amp; accessories. All package system comes with full one year warranty. Extended warranty for up to 5 years is also available*.</p>
    </div>
    <div class="about-photo" role="img" aria-label="Photo of a PC with monitor showing camera feeds, keyboard and two dome security cameras"></div>
  </section>

  <section class="panel panel-packages"></section>

  <section class="panel panel-visit">
    <div class="visit-band">
      <p class="visit-label">Visit us:</p>
      <p class="visit-url">www.brightwardsecure.com.au</p>
    </div>
    <div class="visit-photo" role="img" aria-label="Photo of a monitor showing security camera views of a shop"></div>
    <div class="visit-rule"></div>
    <p class="visit-text">We offer a variety of CCTV system packages that are reliable, affordable and easy to use. Below are some of the packages that are suitable for a home or small business. If you need a system with more than 4 cameras or have a special need please contact us for a free quote and we will ensure you will be happy and satisfied with our product, service and prices.</p>
  </section>

  <svg class="visit-icon" viewBox="0 0 54 54"><circle cx="27" cy="27" r="26" fill="#ffffff"/><circle cx="27" cy="27" r="20" fill="var(--yellow-band)"/><circle cx="27" cy="27" r="16" fill="none" stroke="#ffffff" stroke-width="2.5"/><path d="M18 27h16M27 20l7 7-7 7" fill="none" stroke="#ffffff" stroke-width="3" stroke-linecap="round" stroke-linejoin="round"/></svg>

  <h1 class="packages-title">Packages</h1>

  <div class="package-sheet">
    <div class="package-row package-row-dvr">
      <article class="package">
        <h3 class="package-name">Package 1</h3>
        <p class="package-type">Standalone DVR System (2 Cameras)</p>
        <div class="package-photo" role="img" aria-label="Monitor, DVR recorder and two dome cameras"></div>
        <div class="package-rule rule-top"></div>
        <ul class="package-specs"><li>2 X high resolution dome cameras</li><li>1 X 4 channel standalone DVR</li><li>500GB hard drive</li><li>19" LCD monitor</li><li>Remote access from PCs &amp; Phones*</li><li>Easy to use</li><li>1 Year Warranty</li><li>Full system supplied &amp; installed</li></ul>
        <div class="package-rule rule-bottom"></div>
        <p class="package-price">$1495</p><p class="package-gst">+ GST*</p>
        <div class="package-contact">Contact Us</div>
      </article>
      <article class="package">
        <h3 class="package-name">Package 2</h3>
        <p class="package-type">Standalone DVR System (4 Cameras)</p>
        <div class="package-photo" role="img" aria-label="Monitor, DVR recorder and four dome cameras"></div>
        <div class="package-rule rule-top"></div>
        <ul class="package-specs"><li>4 X high resolution dome cameras</li><li>1 X 4 channel standalone DVR</li><li>500GB hard drive</li><li>19" LCD monitor</li><li>Remote access from PCs &amp; Phones*</li><li>Easy to use</li><li>1 Year Warranty</li><li>Full system supplied &amp; installed</li></ul>
        <div class="package-rule rule-bottom"></div>
        <p class="package-price">$2195</p><p class="package-gst">+ GST*</p>
        <div class="package-contact">Contact Us</div>
      </article>
      <article class="package">
        <h3 class="package-name">Package 3</h3>
        <p class="package-type">Standalone DVR System (8 Cameras)</p>
        <div class="package-photo" role="img" aria-label="Monitor, DVR recorder and eight dome cameras"></div>
        <div class="package-rule rule-top"></div>
        <ul class="package-specs"><li>8 X high resolution dome cameras</li><li>1 X 8 channel standalone DVR</li><li>1 Terrabyte hard drive</li><li>19" LCD monitor</li><li>Remote access from PCs &amp; Phones*</li><li>Easy to use</li><li>1 Year Warranty</li><li>Full system supplied &amp; installed</li></ul>
        <div class="package-rule rule-bottom"></div>
        <p class="package-price">$3295</p><p class="package-gst">+ GST*</p>
        <div class="package-contact">Contact Us</div>
      </article>
    </div>

    <div class="package-row package-row-ip">
      <article class="package">
        <h3 class="package-name">Package 4</h3>
        <p class="package-type">IP based CCTV System (2 Cameras)</p>
        <div class="package-photo" role="img" aria-label="PC with monitor and two IP dome cameras"></div>
        <div class="package-rule rule-top"></div>
        <ul class="package-specs"><li>2 X 2 Megapixel IP Cameras</li><li>1 X PC based NVR System</li><li>500GB hard drive</li><li>19" LCD Monitor</li><li>Remote Access from PCs and Phones*</li><li>Easy to use</li><li>1 Year warranty</li><li>Full system supplied &amp; Installed</li></ul>
        <div class="package-rule rule-bottom"></div>
        <p class="package-price">$1995</p><p class="package-gst">+ GST*</p>
        <div class="package-contact">Contact Us</div>
      </article>
      <article class="package">
        <h3 class="package-name">Package 5</h3>
        <p class="package-type">IP based CCTV System (4 Cameras)</p>
        <div class="package-photo" role="img" aria-label="PC with monitor and four IP dome cameras"></div>
        <div class="package-rule rule-top"></div>
        <ul class="package-specs"><li>4 X 2 Megapixel IP Cameras</li><li>1 X PC based NVR System</li><li>1 Terrabyte hard drive</li><li>19" LCD Monitor</li><li>Remote Access from PCs and Phones*</li><li>Easy to use</li><li>1 Year warranty</li><li>Full system supplied &amp; Installed</li></ul>
        <div class="package-rule rule-bottom"></div>
        <p class="package-price">$3295</p><p class="package-gst">+ GST*</p>
        <div class="package-contact">Contact Us</div>
      </article>
      <article class="package">
        <h3 class="package-name">Package 6</h3>
        <p class="package-type">IP based CCTV System (8 Cameras)</p>
        <div class="package-photo" role="img" aria-label="PC with monitor and eight IP dome cameras"></div>
        <div class="package-rule rule-top"></div>
        <ul class="package-specs"><li>8 X 2 Megapixel IP Cameras</li><li>1 X PC based NVR System</li><li>2 Terrabyte hard drive</li><li>19" LCD Monitor</li><li>Remote Access from PCs and Phones*</li><li>Easy to use</li><li>1 Year warranty</li><li>Full system supplied &amp; Installed</li></ul>
        <div class="package-rule rule-bottom"></div>
        <p class="package-price">$4495</p><p class="package-gst">+ GST*</p>
        <div class="package-contact">Contact Us</div>
      </article>
    </div>
  </div>

</main>
</body>
</html>
```